Law Firm Specializing In Long-Term Care Negligence Needs a New Website

We have been using the same website for about 10 years. We need a new, fresh website design that will help us attract new clients. Many of our clients find us through Google search and the website is the first contact with the firm. Our current website is www.tarvelinlaw.com. We want to continue to have good placement on Google search using the terms that are currently used in the website. We have been on Google search for a long time and have good SEO placement without spending money on SEO optimization. Need to stand out from the competition. We are the only law firm in North Carolina that only handles cases involving long-term care negligence.

Target Market(s)

Individuals searching for an attorney who specializes in cases involving long-term care negligence. Cases against nursing homes, assisted living facilities, group homes.

Industry/Entity Type

Law Firm

Logo Text

Tarvelin Law

Coding

Coded - Design and coding required

Number of Pages Required

5+ page

Requirements
Must have
• I would like to have the same pages that I currently have on my website. I am trying to freshen up the website.

```html
<!DOCTYPE html>
<html lang="en">
<head>
<meta charset="utf-8">
<title>Tarvelin Law</title>
<link href="https://fonts.googleapis.com/css2?family=Lato:wght@300;400;700&family=Oswald:wght@400;500&display=swap" rel="stylesheet">
<style>
:root{
  --olive:#8b8561;
  --olive-dark:#6f6a4b;
  --olive-light:#b3ad86;
  --ink:#1d1d1b;
  --charcoal:#2a2a27;
  --text:#555;
  --white:#fff;
}
*{box-sizing:border-box;margin:0;padding:0}
html,body{width:845px;height:1200px;overflow:hidden}
body{font-family:"Lato",sans-serif;color:var(--text);background:var(--white);font-size:8px;line-height:1.5}
.site-header{height:22px;background:var(--ink);display:flex;align-items:center;gap:6px;padding:0 155px}
.brand-mark{width:8px;height:8px;background:var(--olive)}
.brand{font-family:"Lato",sans-serif;color:var(--white);font-size:12px;font-weight:400}
.main-nav{height:30px;background:var(--olive);display:flex;align-items:center;justify-content:center;gap:4px;padding:0 80px}
.main-nav a{color:var(--white);text-decoration:none;font-size:8px;letter-spacing:.5px;padding:6px 16px;text-transform:uppercase}
.main-nav a.active{background:var(--white);color:var(--olive-dark);font-weight:700}
.hero{position:relative;height:232px;background:linear-gradient(90deg,#1b1a16 0%,#3a362b 55%,#6b6250 80%,#3b372c 100%);padding:50px 172px 0}
.hero-copy{position:relative;max-width:300px;color:var(--white)}
.hero h1{font-family:"Oswald",sans-serif;font-size:26px;font-weight:400;letter-spacing:1px;margin-bottom:8px}
.hero p{font-size:8px;line-height:1.6;margin-bottom:14px;opacity:.9}
.btn{display:inline-block;font-size:9px;text-transform:uppercase;padding:7px 16px;letter-spacing:.5px;border:none}
.btn-light{background:var(--white);color:var(--ink)}
.btn-olive{background:var(--olive);color:var(--white)}
.hero-photo{position:absolute;inset:0}
.accent-bar{height:8px;background:var(--olive)}
.welcome{padding:32px 80px 30px;text-align:center;height:192px}
.section-title{font-family:"Lato",sans-serif;font-weight:300;font-size:24px;color:var(--olive);letter-spacing:1px;margin-bottom:12px}
.welcome p{max-width:680px;margin:0 auto 14px;font-size:7.5px;line-height:1.7}
.practice{position:relative;height:322px;background:linear-gradient(180deg,#23231f,#171714);text-align:center;padding:30px 120px 0;color:var(--white)}
.practice .section-title{color:var(--olive-light)}
.practice .lead{max-width:520px;margin:0 auto 24px;font-size:7.5px;opacity:.85}
.areas{display:flex;justify-content:space-between}
.area{width:150px}
.area-icon{width:56px;height:56px;border-radius:50%;background:var(--olive);margin:0 auto 10px;display:flex;align-items:center;justify-content:center}
.area h3{font-size:9px;font-weight:400;letter-spacing:.5px;margin-bottom:6px;text-transform:uppercase}
.area p{font-size:7px;opacity:.8}
.contact{display:flex;gap:50px;padding:22px 190px 0 155px;height:228px}
.meeting{width:250px}
.meeting-photo{height:150px;background:linear-gradient(135deg,#c9c3b6,#8c8273 55%,#5b5448)}
.meeting p{font-size:7px;margin-top:8px}
.ask{flex:1}
.ask h2{font-weight:300;font-size:13px;color:var(--ink);letter-spacing:1px;margin-bottom:8px;white-space:nowrap}
.field{border:1px solid #ccc;height:18px;margin-bottom:5px;font-size:7px;color:#999;padding:4px 7px}
.field.message{height:44px}
.ask .btn{padding:5px 14px}
.site-footer{background:var(--charcoal);height:150px;padding:20px 150px 0 155px;display:flex;gap:40px;color:#ccc}
.foot-col{flex:1}
.foot-col h4{color:var(--white);font-size:8px;font-weight:700;letter-spacing:.5px;margin-bottom:8px;text-transform:uppercase}
.foot-col ul{list-style:none}
.foot-col li{font-size:7px;margin-bottom:3px}
.foot-col li::before{content:"›";color:var(--olive);margin-right:5px}
.socials{display:flex;gap:5px;margin-top:4px}
.socials span{width:13px;height:13px;border-radius:50%;background:#777}
.news-field{height:14px;background:var(--white);margin-bottom:4px;font-size:6.5px;color:#999;padding:2px 5px}
.btn-small{background:var(--white);color:var(--ink);font-size:6.5px;padding:2px 7px;display:inline-block}
.copyright{height:20px;background:var(--olive);color:var(--white);font-size:7px;text-align:center;line-height:20px}
</style>
</head>
<body>
<header class="site-header"><span class="brand-mark"></span><div class="brand">Tarvelin Law</div></header>
<nav class="main-nav">
  <a class="active">Home</a><a>About Us</a><a>Practice Areas</a><a>Our Team</a><a>Resources</a><a>News</a><a>Contact Us</a>
</nav>

<section class="hero">
  <div class="hero-photo" role="img" aria-label="Lawyer at a desk beside scales of justice, dimmed"></div>
  <div class="hero-copy">
    <h1>LOREM IPSUM DUMMY</h1>
    <p>Families trust us when a loved one is harmed in long-term care. We hold nursing homes and care facilities accountable for neglect and abuse across the state.</p>
    <span class="btn btn-light">Read More</span>
  </div>
</section>
<div class="accent-bar"></div>

<section class="welcome">
  <h2 class="section-title">WELCOME TO OUR FIRM</h2>
  <p>Tarvelin Law is the only firm in North Carolina that handles cases involving long-term care negligence alone. For many years we have represented residents and families harmed by nursing homes, assisted living facilities and group homes. We investigate every claim with care, work with medical experts and pursue fair results for those who were let down by the people paid to protect them. Our team listens first, explains each step plainly and stays with you from the first call until the case is resolved.</p>
  <span class="btn btn-olive">Read More</span>
</section>

<section class="practice">
  <h2 class="section-title">WELCOME TO OUR FIRM</h2>
  <p class="lead">We focus on one area of law so we can do it well. Learn about the kinds of cases we take on and how we can help your family.</p>
  <div class="areas">
    <div class="area">
      <div class="area-icon"><svg width="26" height="26" viewBox="0 0 26 26" fill="#fff"><rect x="4" y="8" width="12" height="5" rx="1" transform="rotate(-40 10 10)"/><rect x="12" y="12" width="3" height="12" rx="1" transform="rotate(-40 13 18)"/><rect x="3" y="21" width="12" height="3"/></svg></div>
      <h3>Insurance Law</h3>
      <p>Help with claims and coverage disputes after harm in a care facility or home.</p>
    </div>
    <div class="area">
      <div class="area-icon"><svg width="26" height="26" viewBox="0 0 26 26"><text x="13" y="20" text-anchor="middle" font-family="Lato,sans-serif" font-size="20" font-weight="700" fill="#fff">$</text></svg></div>
      <h3>Property Law</h3>
      <p>Protecting the assets and property of residents from loss or misuse by others.</p>
    </div>
    <div class="area">
      <div class="area-icon"><svg width="26" height="26" viewBox="0 0 26 26" fill="none" stroke="#fff" stroke-width="2.2"><circle cx="12" cy="4" r="2" fill="#fff" stroke="none"/><path d="M12 7v7h6l3 6"/><circle cx="11" cy="17" r="6"/></svg></div>
      <h3>Workplace Law</h3>
      <p>Cases tied to poor staffing, training and care standards in long-term facilities.</p>
    </div>
  </div>
</section>

<section class="contact">
  <div class="meeting">
    <div class="meeting-photo" role="img" aria-label="Attorneys meeting with clients around a table"></div>
    <p>Speak with our team about your case. The first meeting is free and confidential.</p>
  </div>
  <div class="ask">
    <h2>ASK US A QUESTION</h2>
    <div class="field">Name</div>
    <div class="field">Email</div>
    <div class="field">Phone</div>
    <div class="field message">Message</div>
    <span class="btn btn-olive">Submit</span>
  </div>
</section>

<footer class="site-footer">
  <div class="foot-col"><h4>Main Menu</h4><ul><li>Home</li><li>About Us</li><li>Practice Areas</li><li>Our Team</li><li>Resources</li><li>News</li><li>Contact Us</li></ul></div>
  <div class="foot-col"><h4>Quick Links</h4><ul><li>Common Cases</li><li>Nursing Homes</li><li>Assisted Living</li><li>Testimonials</li><li>Sitemap</li></ul></div>
  <div class="foot-col"><h4>Services</h4><ul><li>Free Review</li></ul><h4 style="margin-top:10px">Follow Us On</h4><div class="socials"><span></span><span></span><span></span><span></span></div></div>
  <div class="foot-col"><h4>Newsletter</h4><p style="font-size:7px;margin-bottom:5px">Get updates from our firm.</p><div class="news-field">Your Name</div><div class="news-field">Your Email</div><span class="btn-small">Submit</span></div>
</footer>
<div class="copyright">Copyright © Tarvelin Law. All Rights Reserved.</div>
</body>
</html>
```